Calderwood Membership Company need a book cover designing. The book is called "Harvest T...

Please submit it as a jpg at 300 dpi with A5 dimensions (14.8 cm wide by 21 cm high), and make sure that your text is well within the trim line - approximately 2 cm from the edge. We like the style "Harvest" is written in the attached image, although this is a guideline. It CANNOT be copied, but it may provide influence and inspiration. We are looking for a crisp and clean book cover, so probably on a white background.Our Logo is also attached and we see this being included centered at the bottom "There is a better way to grow your savings" is what the book is about

```html
<!DOCTYPE html>
<html lang="en">
<head>
<meta charset="utf-8">
<title>Harvest Tom — Book Cover</title>
<link rel="stylesheet" href="https://fonts.googleapis.com/css2?family=Caveat:wght@500&family=Josefin+Sans:wght@400;600&display=swap">
<style>
  :root {
    --bg: #e3f6fc;
    --ink: #1c2b50;
    --bar: #8ec6d0;
    --arrow: #e0231d;
    --axis: #c9d8de;
    --label: #9aa9b0;
  }
  html, body {
    margin: 0;
    padding: 0;
    overflow: hidden;
  }
  .cover {
    position: relative;
    width: 800px;
    height: 1200px;
    background: var(--bg);
    overflow: hidden;
    color: var(--ink);
  }
  .cover-title {
    position: absolute;
    top: 105px;
    left: 0;
    width: 800px;
    margin: 0;
    text-align: center;
    font-family: "Caveat", cursive;
    font-weight: 500;
    font-size: 170px;
    line-height: 1;
  }
  .cover-author {
    position: absolute;
    top: 300px;
    left: 0;
    width: 800px;
    margin: 0;
    text-align: center;
    font-family: "Josefin Sans", sans-serif;
    font-weight: 400;
    font-size: 48px;
    letter-spacing: 52px;
    text-indent: 52px;
  }
  .growth-chart {
    position: absolute;
    top: 0;
    left: 0;
  }
  .month-label {
    font-family: "Josefin Sans", sans-serif;
    font-size: 11px;
    fill: var(--label);
    font-style: italic;
  }
  .publisher-mark {
    position: absolute;
    top: 1052px;
    left: 0;
    width: 800px;
    display: flex;
    justify-content: center;
    align-items: center;
    gap: 14px;
  }
  .publisher-dot {
    width: 62px;
    height: 62px;
    border-radius: 50%;
    background: var(--ink);
  }
  .publisher-name {
    font-family: "Josefin Sans", sans-serif;
    font-weight: 600;
    font-size: 34px;
    letter-spacing: 2px;
    color: var(--ink);
  }
</style>
</head>
<body>
<main class="cover">
  <h1 class="cover-title">Harvest</h1>
  <p class="cover-author">TOM</p>

  <svg class="growth-chart" width="800" height="1200" viewBox="0 0 800 1200" aria-hidden="false">
    <defs>
      <linearGradient id="hourglass-tone" x1="0" y1="0" x2="0" y2="1">
        <stop offset="0" stop-color="#b8885c"/>
        <stop offset="0.5" stop-color="#d9cdb4"/>
        <stop offset="1" stop-color="#a7794f"/>
      </linearGradient>
      <linearGradient id="cash-tone" x1="0" y1="0" x2="1" y2="0">
        <stop offset="0" stop-color="#cfd6c2" stop-opacity="0.7"/>
        <stop offset="1" stop-color="#b9c4a8"/>
      </linearGradient>
    </defs>

    <g class="chart-axis" stroke="var(--axis)" stroke-width="1">
      <line x1="80" y1="900" x2="760" y2="900"/>
      <line x1="70" y1="930" x2="770" y2="930"/>
      <line x1="60" y1="955" x2="780" y2="955"/>
    </g>

    <g class="chart-bars" fill="var(--bar)">
      <rect x="153" y="845" width="35" height="25"/>
      <rect x="216" y="817" width="35" height="53"/>
      <rect x="279" y="763" width="35" height="107"/>
      <rect x="340" y="741" width="35" height="129"/>
      <rect x="403" y="714" width="35" height="156"/>
      <rect x="465" y="683" width="35" height="187"/>
      <rect x="526" y="649" width="35" height="221"/>
      <rect x="588" y="608" width="35" height="262"/>
    </g>

    <g class="chart-months">
      <text class="month-label" x="80" y="965">Oct</text>
      <text class="month-label" x="162" y="965">Nov</text>
      <text class="month-label" x="250" y="965">Dec</text>
      <text class="month-label" x="336" y="965">Jan</text>
      <text class="month-label" x="422" y="965">Feb</text>
      <text class="month-label" x="508" y="965">Mar</text>
      <text class="month-label" x="594" y="965">Apr</text>
      <text class="month-label" x="682" y="965">May</text>
    </g>

    <rect class="cash-stacks" x="355" y="860" width="385" height="90" rx="6"
          fill="url(#cash-tone)" role="img"
          aria-label="Stacks of banknotes growing taller from left to right"/>

    <rect class="hourglass" x="75" y="555" width="225" height="385" rx="14"
          fill="url(#hourglass-tone)" role="img"
          aria-label="Wooden hourglass with sand above and banknotes collected below"/>

    <g class="growth-arrow">
      <path d="M125 792 C 290 720, 470 670, 580 530" fill="none" stroke="var(--arrow)" stroke-width="3.5"/>
      <polygon points="600,515 560,532 584,552" fill="var(--arrow)"/>
    </g>
  </svg>

  <div class="publisher-mark">
    <span class="publisher-dot"></span>
    <span class="publisher-name">HARVEST TOM</span>
  </div>
</main>
</body>
</html>
```